I want a double sided flyer possibly with a picture of a lawn or grass.
Company name, phone number, email, and logo
Corvane Lawn Management, (404)672-8154,Corvane_Lawn@brisknet.com
Company services
Fertilization and weed control,Lawn and Landscape maintenance, mowing, pruning, aeration, landscape and Christmas lights,

```html
<!DOCTYPE html>
<html lang="en">
<head>
<meta charset="utf-8">
<title>Corvane Lawn Management Flyer</title>
<link href="https://fonts.googleapis.com/css2?family=Oswald:wght@500&family=Cinzel:wght@500&family=Roboto+Condensed:wght@400;700&display=swap" rel="stylesheet">
<style>
  :root {
    --backdrop: #5f636b;
    --paper: #ffffff;
    --brand-green: #2e8b2a;
    --leaf-green: #3aa335;
    --pill-green: #3fb33a;
    --pill-edge: #2a7d26;
    --sky-blue: #d6e6f3;
    --grass-light: #b8e04a;
    --grass-mid: #5fae25;
    --soil: #2d1d14;
    --rule: #c9d3c9;
  }
  html, body {
    margin: 0;
    width: 1200px;
    height: 1000px;
    overflow: hidden;
    background: var(--backdrop);
  }
  .flyer {
    position: absolute;
    left: 263px;
    top: 25px;
    width: 674px;
    height: 952px;
    background: var(--paper);
    overflow: hidden;
    box-shadow: 0 4px 14px rgba(0,0,0,0.35);
  }
  .sky-photo {
    position: absolute;
    inset: 0 0 auto 0;
    height: 520px;
    background:
      radial-gradient(ellipse 160px 90px at 60px 300px, var(--sky-blue), transparent 70%),
      radial-gradient(ellipse 140px 110px at 620px 200px, var(--sky-blue), transparent 70%),
      radial-gradient(ellipse 200px 80px at 120px 40px, #e6eff7, transparent 70%),
      linear-gradient(#f4f8fb, #ffffff 85%);
  }
  .grass-photo {
    position: absolute;
    left: 0;
    right: 0;
    top: 505px;
    bottom: 0;
    background: linear-gradient(180deg,
      rgba(255,255,255,0) 0%,
      var(--grass-light) 14%,
      var(--grass-mid) 40%,
      #8fc73a 55%,
      #5a7a2a 60%,
      var(--soil) 66%,
      var(--soil) 100%);
  }
  .brand {
    position: absolute;
    left: 0;
    right: 0;
    top: 90px;
    text-align: center;
  }
  .brand-dot {
    display: block;
    margin: 0 auto 60px;
    width: 120px;
    height: 120px;
    border-radius: 50%;
    background: var(--leaf-green);
  }
  .brand-name {
    margin: 0;
    font-family: "Oswald", sans-serif;
    font-weight: 500;
    color: var(--brand-green);
    line-height: 1;
  }
  .brand-name .primary {
    display: block;
    font-size: 78px;
    letter-spacing: 1px;
  }
  .brand-name .secondary {
    display: block;
    margin-top: 6px;
    font-size: 31px;
  }
  .services {
    position: absolute;
    left: 80px;
    right: 80px;
    top: 401px;
    padding: 8px 0 6px;
    border-top: 1px solid var(--rule);
    border-bottom: 1px solid var(--rule);
    margin: 0;
    text-align: center;
    font-family: "Cinzel", serif;
    font-weight: 500;
    font-size: 15.5px;
    line-height: 19px;
    color: var(--brand-green);
  }
  .contact-pill {
    position: absolute;
    left: 80px;
    top: 851px;
    width: 514px;
    height: 34px;
    border-radius: 10px;
    background: linear-gradient(var(--pill-green), #36a131);
    border: 2px solid var(--pill-edge);
    box-sizing: border-box;
    color: #fff;
    font-family: "Roboto Condensed", sans-serif;
    font-size: 21px;
    line-height: 30px;
    text-align: center;
    white-space: nowrap;
  }
  .contact-pill strong { font-weight: 700; }
</style>
</head>
<body>
  <main class="flyer">
    <div class="sky-photo" role="img" aria-label="Photo of a soft blue sky with white clouds"></div>
    <div class="grass-photo" role="img" aria-label="Photo of fresh green grass growing from dark soil, seen in cross-section"></div>

    <header class="brand">
      <span class="brand-dot"></span>
      <h1 class="brand-name">
        <span class="primary">CORVANE</span>
        <span class="secondary">Lawn Management</span>
      </h1>
    </header>

    <p class="services">Fertilization &amp; Weed Control, Lawn &amp; Landscape<br>Maintenance, Mowing, Pruning, Aeration, Landscape<br>and Christmas lights</p>

    <div class="contact-pill">call <strong>(404) 672-8154</strong> or email <strong>Corvane_Lawn@brisknet.com</strong></div>
  </main>
</body>
</html>
```